psd/html for a e wallet payment website designed

hi
i am in need of a psd / html for a whole website designed
the site is a e wallet /payment system i can i will provide a link to what type of style i am looking for but i can not stress this enough i do not want anyone replicating the website i am just providing the links to show you what kind of function and the content that is involved also, i have a srs with detailed pages you can read and refer to if need be
thanks of viewing
Plimvora.com
Quindrel.com
brankowelt.com
Tazurnik.com

```html
<!DOCTYPE html>
<html lang="en">
<head>
<meta charset="utf-8">
<title>E-Wallet</title>
<link rel="stylesheet" href="https://fonts.googleapis.com/css2?family=PT+Serif&family=Ubuntu:wght@400&display=swap">
<style>
:root{
  --page:#f3f3f3;
  --panel:#ffffff;
  --panel-edge:#c9c9c9;
  --ink:#1d1d1d;
  --muted:#555;
  --silver-top:#fbfbfb;
  --silver-bottom:#d6d6d6;
  --dots:#e2e2e2;
  --hero-a:#0d6f86;
  --hero-b:#17a08f;
  --hero-c:#a9d63a;
  --glass:rgba(205,235,245,.72);
  --glass-edge:#eaf6fb;
  --social:#5d5d5d;
  --card:#f1f1f1;
  --card-edge:#9b9b9b;
  --badge:#e4e4e4;
}
*{box-sizing:border-box;margin:0;padding:0}
html,body{width:1200px;height:885px;overflow:hidden}
body{background:var(--page);font-family:"PT Serif",serif;color:var(--ink);position:relative}
.abs{position:absolute}
.site{left:78px;top:90px;width:1058px;height:660px;background:var(--panel);border:1px solid var(--panel-edge);border-radius:18px;box-shadow:0 3px 8px rgba(0,0,0,.18);overflow:hidden}
.header{left:0;top:0;width:100%;height:126px;background:linear-gradient(#fff 0%,#fafafa 55%,#e3e3e3 100%)}
.header-band{left:0;top:94px;width:100%;height:32px;background:var(--dots)}
.footer-band{left:0;top:628px;width:100%;height:32px;background:var(--dots)}
.brand-mark{left:103px;top:113px;width:70px;height:72px;background:#9a9a9a;border-radius:4px}
.brand-name{left:180px;top:112px;font-size:34px;line-height:35px;color:#2a2a2a}
.brand-name span{display:block;font-size:40px;line-height:38px}
.field{left:935px;width:170px;height:24px;background:#fff;border:1px solid #c4c4c4;border-radius:2px;font-family:"Ubuntu",sans-serif;font-size:10px;color:#8a8a8a;padding:5px 6px}
.field .btn{position:absolute;right:-1px;top:-1px;width:32px;height:24px;background:linear-gradient(#bdbdbd,#8f8f8f)}
.nav{left:78px;top:217px;width:1058px;height:35px;background:linear-gradient(var(--silver-top),var(--silver-bottom));border-top:1px solid #fff;border-bottom:1px solid #b9b9b9}
.nav-item{top:226px;font-size:14px;transform:translateX(-50%);white-space:nowrap}
.nav-sep{top:223px;width:1px;height:22px;background:#b7b7b7;box-shadow:1px 0 #fff}
.hero{left:78px;top:253px;width:1058px;height:287px;background:linear-gradient(160deg,var(--hero-b) 0%,var(--hero-a) 45%,#1690b9 100%),var(--hero-a)}
.hero-glow{left:78px;top:330px;width:800px;height:210px;background:linear-gradient(10deg,var(--hero-c) 0%,rgba(150,210,60,.5) 40%,rgba(23,160,143,0) 80%)}
.caption{left:78px;top:479px;width:1058px;height:61px;background:rgba(230,245,240,.55)}
.caption p{position:absolute;left:87px;top:9px;width:900px;font-size:13.5px;line-height:19px;color:#1b1b1b}
.login{left:916px;top:262px;width:224px;height:208px;background:var(--glass);border:2px solid var(--glass-edge);border-radius:10px;padding:10px 7px;font-size:15px}
.login .tabs{display:flex;gap:14px;align-items:center}
.login .tabs i{width:1px;height:20px;background:#fff}
.login label{display:block;margin-top:12px}
.login .input{height:16px;background:#fff;border:1px solid #9ec7d4;margin-top:2px}
.login .rule{height:1px;background:#fff;margin-top:8px}
.login .submit{margin-top:6px;display:flex;align-items:center;gap:6px}
.social{left:1136px;top:253px;width:29px;height:202px;background:var(--social);border-radius:0 3px 3px 0}
.card{top:545px;height:177px;background:var(--card);border:1px solid var(--card-edge);border-radius:0 0 8px 8px;overflow:hidden}
.card h2{font-weight:400;font-size:21px;position:absolute;left:8px;top:5px}
.card .rule{position:absolute;left:7px;right:8px;top:33px;height:2px;border-top:1px solid #aaa;border-bottom:1px solid #fff}
.card .art{position:absolute;right:10px;top:6px;width:70px;height:80px;border-radius:8px}
.card p{position:absolute;left:8px;top:40px;width:165px;font-size:10.5px;line-height:14.6px;text-align:justify}
.card .signup{position:absolute;left:0;bottom:0;width:100%;height:25px;background:linear-gradient(#fafafa,#cfcfcf);border-top:1px solid #aaa;text-align:center;font-size:14px;line-height:24px}
.news{left:682px;top:545px;width:430px;height:177px;background:var(--card);border:1px solid var(--card-edge);border-radius:0 0 8px 8px;padding:6px 12px}
.news h2{font-weight:400;font-size:21px}
.news p{font-size:10px;line-height:14.5px;margin-top:4px}
.badge{top:765px;height:46px;background:var(--badge);border-radius:3px}
.footer-links{right:74px;top:786px;display:flex;font-family:"Ubuntu",sans-serif;font-size:9px;color:#555}
.footer-links span{padding:0 8px;border-left:1px solid #bbb}
.footer-links span:first-child{border-left:none}
</style>
</head>
<body>
<div class="abs site">
  <div class="abs header"></div>
  <div class="abs header-band"></div>
  <div class="abs footer-band"></div>
</div>

<div class="abs brand-mark" role="img" aria-label="Safe illustration beside the wallet name"></div>
<div class="abs brand-name">E-Wallet<span>Logo</span></div>

<div class="abs field" style="top:153px">Select Language<div class="btn">
  <svg width="32" height="24"><path d="M10 9h12l-6 7z" fill="#fff"/></svg></div></div>
<div class="abs field" style="top:181px">Search_<div class="btn">
  <svg width="32" height="24"><circle cx="15" cy="11" r="4" fill="none" stroke="#fff" stroke-width="2"/><path d="M18 14l4 4" stroke="#fff" stroke-width="2"/></svg></div></div>

<nav class="abs nav"></nav>
<div class="abs nav-item" style="left:235px">Home</div>
<div class="abs nav-sep" style="left:290px"></div>
<div class="abs nav-item" style="left:360px">About Us</div>
<div class="abs nav-sep" style="left:441px"></div>
<div class="abs nav-item" style="left:528px">Personal Account</div>
<div class="abs nav-sep" style="left:617px"></div>
<div class="abs nav-item" style="left:702px">Business Account</div>
<div class="abs nav-sep" style="left:786px"></div>
<div class="abs nav-item" style="left:844px">Guides</div>
<div class="abs nav-sep" style="left:912px"></div>
<div class="abs nav-item" style="left:972px">Contact Us</div>

<div class="abs hero" role="img" aria-label="Abstract flowing light waves in teal and green"></div>
<div class="abs hero-glow"></div>
<div class="abs caption">
  <p>Whether you're a traditional brick-and-mortar looking to expand online, or a new business venture seeking the most convenient way to develop or enhance your web presence, Ewallet complete suite of customizable business tools will help your business thrive in today's evolution-Commerce.</p>
</div>
<svg class="abs" style="left:100px;top:493px" width="20" height="30"><path d="M18 2v26L2 15z" fill="#fff"/></svg>
<svg class="abs" style="left:1100px;top:493px" width="20" height="30"><path d="M2 2v26l16-13z" fill="#fff"/></svg>

<form class="abs login">
  <div class="tabs"><span>Login</span><i></i><span>Register</span></div>
  <label>Name</label><div class="input"></div>
  <label>Email</label><div class="input"></div>
  <div class="rule"></div>
  <div class="submit">Login <svg width="14" height="18"><path d="M2 1v16l10-8z" fill="#fff"/></svg></div>
  <div class="rule" style="margin-top:10px"></div>
</form>

<div class="abs social">
  <svg width="29" height="202">
    <circle cx="14" cy="26" r="8" fill="#e9e9e9"/>
    <circle cx="14" cy="74" r="8" fill="#e9e9e9"/>
    <g fill="none" stroke="#e9e9e9" stroke-width="2.5"><path d="M6 116a14 14 0 0 1 14 14"/><path d="M6 122a8 8 0 0 1 8 8"/></g>
    <circle cx="7.5" cy="129" r="2" fill="#e9e9e9"/>
    <rect x="4" y="168" width="20" height="14" fill="#e9e9e9"/>
    <path d="M4 168l10 8 10-8" fill="none" stroke="#5d5d5d" stroke-width="1.2"/>
  </svg>
</div>

<section class="abs card" style="left:135px;width:265px">
  <h2>Shopping Online</h2><div class="rule"></div>
  <div class="art" role="img" aria-label="Shopping basket with add symbol" style="background:linear-gradient(#f6a23a,#e0601a)"></div>
  <p>Lorem ipsum dolor sit amet, consectetuer adipiscing elit, sed diam nonummy nibh euismod tincidunt ut laoreet dolore magna aliquam erat volutpat. Ut wisi enim ad minim veniam, quis nostrud exerci tation ullamcorper</p>
  <div class="signup">Sign Up</div>
</section>
<section class="abs card" style="left:410px;width:265px">
  <h2>Selling Online</h2><div class="rule"></div>
  <div class="art" role="img" aria-label="Globe with coin stacks and arrow" style="background:linear-gradient(#6fb7dc,#c9c9c9)"></div>
  <p>Lorem ipsum dolor sit amet, consectetuer adipiscing elit, sed diam nonummy nibh euismod tincidunt ut laoreet dolore magna aliquam erat volutpat. Ut wisi enim ad minim veniam, quis nostrud exerci tation ullamcorper</p>
  <div class="signup">Sign Up</div>
</section>
<section class="abs news">
  <h2>Updates News</h2>
  <p>Lorem ipsum dolor sit amet, consectetuer adipiscing elit, sed diam nonummy nibh euismod tincidunt ut laoreet dolore magna aliquam erat volutpat. Ut wisi enim ad minim veniam, quis nostrud exerci tation ullamcorper suscipit lobortis nisl ut aliquip ex ea commodo consequat. Duis autem vel eum iriure dolor in hendrerit in vulputate velit esse molestie consequat, vel illum dolore eu feugiat nulla facilisis at vero eros et accumsan et iusto odio dignissim qui blandit praesent luptatum zzril delenit augue duis dolore te feugait nulla facilisi. Nam liber tempor cum soluta nobis eleifend option congue nihil imperdiet doming id quod mazim placerat facer possim assum.</p>
</section>

<div class="abs badge" style="left:95px;width:82px"></div>
<div class="abs badge" style="left:183px;width:100px"></div>
<div class="abs badge" style="left:290px;width:80px"></div>

<div class="abs footer-links">
  <span>Security Zone</span><span>User Agreement</span><span>Privacy Policy</span><span>Sitemap</span><span>Disclaimer</span><span>Copyrights C 2007 ewallet company</span>
</div>
</body>
</html>
```